Kestrel Lane flyer

Need a A6 size horizontal layout flyer. See attached example for ideas as well as some images I have which you can use. we are a hire car company that provides vehicles to clients who have recently been involved in car accidents and who's cars are currently getting fixed and so they lose the use of their own vehicle. see our website to keep flyer in line with website and for any further information kestrellane.com.au

Target Market(s)

people involved in not at fault car accidents

Industry/Entity Type

It Company

Requirements
Must have
• *ask people to let us know where they got our flyer from when they call us
• *call to action for people to call our phone number 1800 417 582
Should not have
• any mentioning that the vehicle is free

```html
<!DOCTYPE html>
<html lang="en">
<head>
<meta charset="UTF-8">
<title>Kestrel Lane – Accident Replacement Flyer</title>
<link href="https://fonts.googleapis.com/css2?family=Fira+Sans:wght@400;500;600;700&family=Fira+Sans+Condensed:wght@500;600;700&display=swap" rel="stylesheet">
<style>
  :root {
    --blue-deep: #1b4fa6;
    --blue-mid: #2a6ec8;
    --blue-bright: #1f9be0;
    --blue-light: #5b93d6;
    --blue-pale: #8fb6e6;
    --yellow: #fbb515;
    --white: #ffffff;
    --photo-dark: #4a4d50;
    --photo-light: #c9ccce;
  }
  * { margin: 0; padding: 0; box-sizing: border-box; }
  html, body { width: 1200px; height: 871px; overflow: hidden; background: #ffffff; }
  .flyer {
    position: relative;
    width: 1200px;
    height: 871px;
    overflow: hidden;
    font-family: "Fira Sans", Arial, sans-serif;
    color: var(--white);
  }
  .flyer__backdrop { position: absolute; inset: 0; }

  .brand {
    position: absolute;
    left: 620px;
    top: 100px;
    width: 270px;
    text-align: center;
    font-size: 44px;
    font-weight: 600;
    letter-spacing: 0.5px;
    line-height: 1;
    padding-top: 40px;
  }

  .ownership {
    position: absolute;
    left: 928px;
    top: 126px;
    display: flex;
    align-items: center;
    gap: 12px;
  }
  .ownership__mark {
    width: 66px;
    height: 58px;
    background: var(--white);
    border-radius: 4px;
  }
  .ownership__figure { font-size: 30px; font-weight: 700; line-height: 1; }
  .ownership__label { font-size: 14px; font-weight: 400; line-height: 1.2; }

  .headline {
    position: absolute;
    left: 640px;
    top: 236px;
    width: 500px;
    text-align: center;
    font-size: 30px;
    font-weight: 600;
    line-height: 1.38;
  }
  .headline__accent { color: var(--yellow); }

  .steps {
    position: absolute;
    left: 650px;
    top: 374px;
    display: flex;
    gap: 18px;
  }
  .step {
    width: 162px;
    height: 162px;
    border-radius: 50%;
    border: 6px solid var(--white);
    display: flex;
    flex-direction: column;
    align-items: center;
    justify-content: center;
    text-align: center;
    text-transform: uppercase;
    font-family: "Fira Sans Condensed", Arial, sans-serif;
    font-weight: 600;
    box-shadow: 0 10px 14px rgba(10, 40, 90, 0.35);
  }
  .step--call { background: var(--yellow); font-size: 15px; line-height: 1.2; }
  .step--details { background: var(--blue-light); font-size: 18px; line-height: 1.1; }
  .step--vehicle { background: var(--blue-mid); font-size: 16px; line-height: 1.15; }
  .step__icon { width: 28px; height: 24px; margin-bottom: 6px; }

  .offer {
    position: absolute;
    left: 768px;
    top: 584px;
  }
  .offer__title {
    color: var(--yellow);
    font-size: 26px;
    font-weight: 500;
    text-transform: uppercase;
    letter-spacing: 0.3px;
  }
  .offer__list { list-style: none; margin: 18px 0 0 46px; }
  .offer__item {
    display: flex;
    align-items: center;
    gap: 12px;
    font-size: 23px;
    font-weight: 500;
    text-transform: uppercase;
    margin-bottom: 16px;
  }
  .offer__tick { width: 28px; height: 28px; flex: none; }

  .website {
    position: absolute;
    right: 30px;
    top: 760px;
    font-size: 24px;
    font-weight: 700;
    letter-spacing: 0.3px;
  }

  .callout {
    position: absolute;
    left: 432px;
    top: 806px;
    width: 768px;
    height: 65px;
    background: var(--yellow);
    border-radius: 12px 0 0 12px;
    display: flex;
    align-items: center;
    padding-left: 22px;
    font-family: "Fira Sans Condensed", Arial, sans-serif;
  }
  .callout__prompt { font-size: 27px; font-weight: 600; }
  .callout__icon { width: 30px; height: 30px; margin: 0 26px 0 12px; }
  .callout__number { font-size: 40px; font-weight: 700; letter-spacing: 0.5px; }
</style>
</head>
<body>
<main class="flyer">
  <svg class="flyer__backdrop" width="1200" height="871" viewBox="0 0 1200 871">
    <defs>
      <radialGradient id="panelGlow" cx="0.62" cy="0.45" r="0.7">
        <stop offset="0" stop-color="#1aa9ea"/>
        <stop offset="0.45" stop-color="#1f78cf"/>
        <stop offset="1" stop-color="#1a4aa2"/>
      </radialGradient>
      <linearGradient id="photoTone" x1="0" y1="0" x2="1" y2="1">
        <stop offset="0" stop-color="#dfe2e4"/>
        <stop offset="0.45" stop-color="#9a9ea1"/>
        <stop offset="1" stop-color="#55595c"/>
      </linearGradient>
    </defs>
    <rect class="panel" width="1200" height="871" fill="url(#panelGlow)"/>
    <path class="panel-band" d="M300 0 H380 C 540 160, 690 500, 810 871 H770 C 650 500, 480 150, 300 0 Z" fill="#6aa0dc"/>
    <path class="photo-edge" d="M320 0 C 480 150, 660 500, 782 871" fill="none" stroke="#ffffff" stroke-width="14"/>
    <path class="photo-area" role="img" aria-label="Photograph of a white car's headlight and front bumper parked on a shaded tree-lined dirt road"
          d="M0 0 H312 C 470 150, 650 500, 774 871 H0 Z" fill="url(#photoTone)"/>
  </svg>

  <div class="brand">Kestrel Lane</div>

  <div class="ownership">
    <div class="ownership__mark"></div>
    <div>
      <div class="ownership__figure">100%</div>
      <div class="ownership__label">Australian Owned</div>
    </div>
  </div>

  <h1 class="headline">Arranging an accident replacement vehicle <span class="headline__accent">for yourself</span> is easy as 1,2,3</h1>

  <div class="steps">
    <div class="step step--call">
      <svg class="step__icon" viewBox="0 0 24 24"><path d="M6.6 10.8a15.1 15.1 0 0 0 6.6 6.6l2.2-2.2c.3-.3.7-.4 1-.2 1.1.4 2.3.6 3.6.6.6 0 1 .4 1 1V20c0 .6-.4 1-1 1A17 17 0 0 1 3 4c0-.6.4-1 1-1h3.5c.6 0 1 .4 1 1 0 1.3.2 2.5.6 3.6.1.3 0 .7-.2 1z" fill="#fff"/></svg>
      <span>Call us on<br>1800 417 582<br>Free call</span>
    </div>
    <div class="step step--details">
      <svg class="step__icon" viewBox="0 0 28 24"><path d="M2 3h14a2 2 0 0 1 2 2v7a2 2 0 0 1-2 2H8l-4 4v-4H2a2 2 0 0 1-2-2V5a2 2 0 0 1 2-2z" fill="#fff"/><path d="M20 8h6a2 2 0 0 1 2 2v6a2 2 0 0 1-2 2h-1v3l-3-3h-6a2 2 0 0 1-2-2h4a4 4 0 0 0 2-1z" fill="#fff"/></svg>
      <span>Provide<br>accident<br>details</span>
    </div>
    <div class="step step--vehicle">
      <svg class="step__icon" viewBox="0 0 28 24"><path d="M6 4h16l3 7h1a2 2 0 0 1 2 2v6h-3v3h-4v-3H7v3H3v-3H0v-6a2 2 0 0 1 2-2h1zm1.5 2.5L5.5 11h17l-2-4.5zM5 14a1.5 1.5 0 1 0 0 3 1.5 1.5 0 0 0 0-3zm18 0a1.5 1.5 0 1 0 0 3 1.5 1.5 0 0 0 0-3z" fill="#fff"/></svg>
      <span>You get a<br>replacement<br>vehicle</span>
    </div>
  </div>

  <section class="offer">
    <h2 class="offer__title">Accident Replacement Car</h2>
    <ul class="offer__list">
      <li class="offer__item">
        <svg class="offer__tick" viewBox="0 0 28 28"><circle cx="14" cy="14" r="11.5" fill="none" stroke="#fbb515" stroke-width="3"/><path d="M8.5 14.5l4 4 7.5-8" fill="none" stroke="#fbb515" stroke-width="3" stroke-linecap="round" stroke-linejoin="round"/></svg>
        Free delivery
      </li>
      <li class="offer__item">
        <svg class="offer__tick" viewBox="0 0 28 28"><circle cx="14" cy="14" r="11.5" fill="none" stroke="#fbb515" stroke-width="3"/><path d="M8.5 14.5l4 4 7.5-8" fill="none" stroke="#fbb515" stroke-width="3" stroke-linecap="round" stroke-linejoin="round"/></svg>
        Late model/new vehicles
      </li>
    </ul>
  </section>

  <div class="website">www.kestrellane.com.au</div>

  <div class="callout">
    <span class="callout__prompt">Tell us where you got this Flyer</span>
    <svg class="callout__icon" viewBox="0 0 30 30"><circle cx="15" cy="15" r="13" fill="none" stroke="#fff" stroke-width="2.5"/><path d="M11 8.5l2.2 3-1.4 1.8a9 9 0 0 0 4.9 4.9l1.8-1.4 3 2.2-1.3 2.5c-5.8-.4-10.3-4.9-10.7-10.7z" fill="#fff"/></svg>
    <span class="callout__number">1800 417 582</span>
  </div>
</main>
</body>
</html>
```